BRISKA sparkling water needs new artwork! Based in Southern California

"Briska" is a new sparkling water company based in Southern California that offers refreshing flavors (lime, cherry, & mango) with B vitamins and antioxidants.

We would like to see packaging designs for standard 12oz cans for each of the three flavors.
Our initial preference is to have individual artwork for each flavor.

Attached are examples of competitors' designs.
Updates

We are extending the deadline for the Thanksgiving Holiday. Thank you all for your contributions.

```html
<!DOCTYPE html>
<html lang="en">
<head>
<meta charset="utf-8">
<title>Briska Sparkling Water – Can Labels</title>
<link href="https://fonts.googleapis.com/css2?family=Archivo:wdth,wght@62..125,400..900&display=swap" rel="stylesheet">
<style>
  :root {
    --canvas: #f1f2f1;
    --white: #ffffff;

    --lime-band: #0f5a2b;
    --lime-body: #f6c300;
    --lime-brand: #0e5a2b;
    --lime-word: #f6d21a;
    --lime-fruit: #ffd93a;

    --cherry-band: #e9ea3b;
    --cherry-body: #d61a2f;
    --cherry-brand: #eceb3d;
    --cherry-word: #d3182c;
    --cherry-fruit: #a3101f;

    --mango-band: #f49b1b;
    --mango-body: #ea4a1f;
    --mango-brand: #ffa21a;
    --mango-word: #c0280f;
    --mango-fruit: #f8a52a;
  }

  * { margin: 0; padding: 0; box-sizing: border-box; }

  html, body {
    width: 800px;
    height: 1200px;
    overflow: hidden;
    background: var(--canvas);
    font-family: "Archivo", Arial, sans-serif;
  }

  .lineup {
    position: absolute;
    top: 280px;
    left: 30px;
    display: flex;
    gap: 25px;
  }

  .label {
    position: relative;
    width: 230px;
    height: 640px;
    overflow: hidden;
    border-radius: 6px;
    background: var(--body);
  }

  .label--lime   { --body: var(--lime-body);   --band: var(--lime-band);   --brand: var(--lime-brand);   --word: var(--lime-word);   --fruit: var(--lime-fruit); }
  .label--cherry { --body: var(--cherry-body); --band: var(--cherry-band); --brand: var(--cherry-brand); --word: var(--cherry-word); --fruit: var(--cherry-fruit); }
  .label--mango  { --body: var(--mango-body);  --band: var(--mango-band);  --brand: var(--mango-brand);  --word: var(--mango-word);  --fruit: var(--mango-fruit); }

  .flavor-band {
    position: absolute;
    top: 0;
    left: 0;
    width: 230px;
    height: 170px;
  }
  .flavor-band path { fill: var(--band); }

  .flavor-name {
    position: absolute;
    top: 62px;
    left: 22px;
    font-size: 40px;
    font-weight: 800;
    letter-spacing: -0.5px;
    color: var(--word);
  }

  .fruit-art {
    position: absolute;
    top: 190px;
    right: 12px;
    width: 86px;
    height: 300px;
    border-radius: 44px;
    background: var(--fruit);
  }

  .brand-name {
    position: absolute;
    left: 8px;
    bottom: 70px;
    writing-mode: vertical-rl;
    transform: rotate(180deg);
    font-size: 104px;
    font-weight: 800;
    font-stretch: 62%;
    line-height: 0.85;
    letter-spacing: -1px;
    color: var(--brand);
  }

  .product-type {
    position: absolute;
    left: 102px;
    bottom: 150px;
    writing-mode: vertical-rl;
    transform: rotate(180deg);
    font-size: 27px;
    font-weight: 500;
    color: var(--white);
  }

  .product-facts {
    position: absolute;
    left: 104px;
    bottom: 26px;
    font-size: 11.5px;
    line-height: 1.2;
    color: var(--white);
  }
  .product-facts::before {
    content: "";
    display: block;
    width: 62px;
    height: 2px;
    margin-bottom: 4px;
    background: var(--brand);
  }
  .label--lime .product-facts::before { background: var(--lime-band); }
</style>
</head>
<body>
  <main class="lineup">

    <section class="label label--lime">
      <svg class="flavor-band" viewBox="0 0 230 170" aria-hidden="true">
        <path d="M0 0 H230 V128 C175 112 125 168 62 150 C32 142 12 150 0 156 Z"/>
      </svg>
      <p class="flavor-name">Lime</p>
      <div class="fruit-art" role="img" aria-label="Illustration of lime slices and leaves"></div>
      <h2 class="brand-name">BRISKA</h2>
      <p class="product-type">Sparkling Water</p>
      <p class="product-facts">Natural Flavors<br>No Added Sugars<br>12fl oz (355ml)</p>
    </section>

    <section class="label label--cherry">
      <svg class="flavor-band" viewBox="0 0 230 170" aria-hidden="true">
        <path d="M0 0 H230 V128 C175 112 125 168 62 150 C32 142 12 150 0 156 Z"/>
      </svg>
      <p class="flavor-name">Cherry</p>
      <div class="fruit-art" role="img" aria-label="Illustration of cherries with stems and leaves"></div>
      <h2 class="brand-name">BRISKA</h2>
      <p class="product-type">Sparkling Water</p>
      <p class="product-facts">Natural Flavors<br>No Added Sugars<br>12fl oz (355ml)</p>
    </section>

    <section class="label label--mango">
      <svg class="flavor-band" viewBox="0 0 230 170" aria-hidden="true">
        <path d="M0 0 H230 V128 C175 112 125 168 62 150 C32 142 12 150 0 156 Z"/>
      </svg>
      <p class="flavor-name">Mango</p>
      <div class="fruit-art" role="img" aria-label="Illustration of a mango and mango slices"></div>
      <h2 class="brand-name">BRISKA</h2>
      <p class="product-type">Sparkling Water</p>
      <p class="product-facts">Natural Flavors<br>No Added Sugars<br>12fl oz (355ml)</p>
    </section>

  </main>
</body>
</html>
```